Website Redesign for Pet Services Facility

We are looking to redesign our current website. The website must be designed in Wix so we can go in and easily edit throughout the life of the website. Design must be professional, simplistic and informative.

Our current website can be found at: www.pawlanelodge.com

I would like the new site to be on one scrolling page. Sections to include:
Home page
Service teaser: Overnight Care, Grooming, Dog Daycare, Retail
An about us area with text on the left and a video on the right
Testimonial section
Overnight Section
Grooming Section
Dog Daycare Section
Retail
Meet the Team
Contact us: address, phone number, hours, etc.
Newsletter sign up and location map

A second page will be used for reservations and should include fields for.
Name, address, phone number, service: Overnight care, grooming, daycare, Arrival date, departure date, pet name, breed, special requests

Our phone number should be easily found through the pages. 'Request a Reservation' buttons should be found throughout page.

Text from our current site can be uesd as a filler for now as I will go in and finalize text when site is complete. Any photos can be used for now as I will go in and choose final photos as a later date.

I started playing with wix and started with a concept that I can share if you are interested, just let me know.

Industry/Entity Type

Pet

Number of Pages Required

2 page

Font styles to use
Sans Serif

Requirements
Must have
• 'Request a Reservation' Buttons
• Phone number easily visible
• location map
• Hours area
• Newsletter sign up

```html
<!DOCTYPE html>
<html lang="en">
<head>
<meta charset="utf-8">
<title>Paw Lane Lodge — Pet Resort</title>
<link rel="stylesheet" href="https://fonts.googleapis.com/css2?family=Arimo:wght@400;700&display=swap">
<style>
  :root {
    --lime: #a9c93a;
    --lime-dark: #7fa82a;
    --button: #8cc63f;
    --teal: #86d0cf;
    --teal-deep: #5fb3b4;
    --teal-light: #d4efec;
    --ink: #2e3327;
    --nav-ink: #3c4219;
    --white: #ffffff;
    --logo-square: #3a3d2c;
  }
  * { box-sizing: border-box; margin: 0; padding: 0; }
  html, body {
    width: 1200px; height: 904px; overflow: hidden;
    background: var(--white);
    font-family: "Arimo", Arial, sans-serif;
    color: var(--ink);
  }
  .site { width: 1200px; height: 904px; position: relative; overflow: hidden; }

  /* Header */
  .site-header { height: 100px; background: var(--lime); position: relative; }
  .brand {
    position: absolute; left: 16px; top: 0; height: 100px;
    display: flex; align-items: center; gap: 10px;
  }
  .brand-mark { width: 64px; height: 100px; background: var(--logo-square); }
  .brand-name {
    font-size: 15px; font-weight: 700; line-height: 1.2;
    color: var(--nav-ink); width: 80px;
  }
  .main-nav {
    position: absolute; left: 182px; right: 24px; bottom: 20px;
    display: flex; justify-content: space-between; white-space: nowrap;
  }
  .main-nav a {
    font-size: 16px; letter-spacing: 2.4px; text-transform: uppercase;
    color: var(--nav-ink); text-decoration: none; white-space: nowrap;
  }
  .call-line {
    position: absolute; top: 14px; right: 40px;
    font-size: 16px; letter-spacing: 2.4px; color: var(--nav-ink); white-space: nowrap;
  }

  /* Hero */
  .hero { height: 556px; position: relative; background: var(--teal); }
  .hero-photo {
    position: absolute; left: 0; top: 0; width: 640px; height: 100%;
    background:
      radial-gradient(ellipse 230px 300px at 420px 330px, var(--teal-light) 0%, rgba(212,239,236,0.55) 45%, rgba(134,208,207,0) 100%),
      linear-gradient(90deg, var(--teal-deep) 0%, var(--teal) 70%, var(--teal) 100%);
  }
  .hero-copy { position: absolute; left: 603px; top: 40px; width: 560px; }
  .hero-title { font-size: 60px; font-weight: 400; line-height: 1.13; color: var(--ink); }
  .hero-text {
    margin-top: 32px; font-size: 17px; line-height: 1.6;
    letter-spacing: 1.3px; text-align: justify; color: var(--ink);
  }
  .reserve-button {
    position: absolute; left: 676px; top: 490px;
    width: 376px; height: 62px; border-radius: 6px;
    background: var(--button); color: var(--white);
    font-size: 21px; letter-spacing: 1px; text-transform: uppercase;
    display: flex; align-items: center; justify-content: center;
    text-decoration: none; border-bottom: 4px solid var(--lime-dark);
  }

  /* About */
  .about { position: relative; height: 248px; background: var(--white); }
  .about-title {
    text-align: center; font-size: 50px; font-weight: 400;
    letter-spacing: 2px; padding-top: 86px; color: var(--ink); line-height: 1;
  }
  .about-column { position: absolute; }
  .about-column h3 { font-size: 34px; font-weight: 400; letter-spacing: 1px; color: var(--ink); line-height: 1; }
  .history { left: 40px; top: 172px; width: 540px; }
  .history p { margin-top: 30px; font-size: 15px; letter-spacing: 0.6px; white-space: nowrap; }
  .video-tour { left: 582px; top: 196px; width: 618px; }
  .video-frame { margin-top: 16px; width: 618px; height: 40px; background: var(--teal); }
</style>
</head>
<body>
<div class="site">
  <header class="site-header">
    <div class="brand">
      <span class="brand-mark"></span>
      <span class="brand-name">Paw Lane Lodge</span>
    </div>
    <nav class="main-nav">
      <a href="#about">About Us</a>
      <a href="#overnight">Overnight Care</a>
      <a href="#grooming">Grooming</a>
      <a href="#daycare">Dog Daycare</a>
      <a href="#retail">Retail</a>
      <a href="#contact">Contact Us</a>
    </nav>
    <p class="call-line">CALL US: 555.014.2290</p>
  </header>

  <section class="hero">
    <div class="hero-photo" role="img" aria-label="Photo of a smiling white dog looking at the camera, tinted teal"></div>
    <div class="hero-copy">
      <h1 class="hero-title">Welcome to<br>Paw Lane Lodge</h1>
      <p class="hero-text">Have your pet experience the most enjoyable resort in the Maple Valley, dedicated to their health and happiness and peace of mind for yourself. We take great pride in treating each and every guest like a member of our family. Take a look around our website and you will find information about everything we have to offer. Thank you for visiting, we hope to meet you and your pet at Paw Lane Lodge.</p>
    </div>
    <a class="reserve-button" href="#reserve">Request a Reservation</a>
  </section>

  <section class="about" id="about">
    <h2 class="about-title">ABOUT US</h2>
    <div class="about-column history">
      <h3>OUR HISTORY</h3>
      <p>In early 2007 we were looking for a place in the Maple Valley for our</p>
    </div>
    <div class="about-column video-tour">
      <h3>VIDEO TOUR</h3>
      <div class="video-frame" role="img" aria-label="Video tour of the lodge"></div>
    </div>
  </section>
</div>
</body>
</html>
```